Website Design for Professional Services Company

• Create a new website design that is easy to maintain inside of WordPress with a main page design, a design for generic content pages, and a design for customer case studies. Our current design relies on a number of plugins to function, and we would like to get away from that as much as possible. Our current design also requires a fair amount of coding that we would like to get away from. The more we can use native WordPress the better. We are not opposed to a small subset of plugins that are widely used and readily updated. Our current website can be found at https://tarnwickconsulting.com/. Our fonts (for use in graphics, we don’t want custom fonts on the website itself to make sure it always displays correctly) and colors are as follows:
o Tarnwick Blue:
 #1b75bc
o Tarnwick Grey:
 #6d6f71
o Main Font:
 Telegrafico
o Accent Font:
 Nexa Light

```html
<!DOCTYPE html>
<html lang="en">
<head>
<meta charset="utf-8">
<title>Tarnwick Consulting — Innovative EPM Solutions</title>
<link rel="stylesheet" href="https://fonts.googleapis.com/css2?family=Poppins:wght@300;400;500;600;700&display=swap">
<style>
:root{
  --brand-blue:#1b75bc;
  --brand-grey:#6d6f71;
  --navy:#1d2a5a;
  --footer:#1f2656;
  --footer-bottom:#2a3270;
  --ink:#2b2f3a;
  --paper:#ffffff;
  --mist:#eef2f7;
}
*{box-sizing:border-box;margin:0;padding:0}
html,body{width:1200px;height:2676px;overflow:hidden}
body{font-family:'Poppins',sans-serif;color:var(--ink);background:var(--paper);position:relative}
.topbar{height:40px;background:var(--brand-blue);color:#fff;font-size:11px;font-weight:500;letter-spacing:.5px;display:flex;align-items:center;padding:0 28px}
.header{height:170px;display:flex;align-items:center;justify-content:space-between;padding:0 90px 0 30px}
.brand{display:flex;flex-direction:column;align-items:center;gap:10px}
.brand-mark{width:54px;height:54px;background:var(--brand-blue)}
.brand-name{font-size:26px;font-weight:600;color:var(--brand-blue);letter-spacing:2px}
.nav{display:flex;gap:34px;font-size:12px;font-weight:500;color:var(--navy);margin-top:-80px}
.nav .active{color:var(--brand-blue)}
.hero{position:absolute;top:210px;left:0;width:1200px;height:490px;background:linear-gradient(100deg,#dfe7f1 0%,#c9d6e6 45%,#aebfd6 100%)}
.hero-copy{position:absolute;right:80px;top:130px;width:600px;text-align:right}
.hero h1{font-size:44px;font-weight:700;color:var(--navy);line-height:1.12}
.hero p{font-size:13px;color:var(--navy);line-height:1.55;margin:22px 0 0 100px;text-align:left}
.btn{display:inline-block;background:var(--brand-blue);color:#fff;font-size:11px;font-weight:600;letter-spacing:.5px;padding:11px 22px;border-radius:4px}
.hero .btn{margin-top:14px}
.services{position:absolute;top:700px;left:0;width:1200px;text-align:center}
.section-title{font-size:26px;font-weight:600;color:var(--navy);margin-top:50px}
.section-sub{font-size:13px;color:var(--brand-grey);margin-top:12px}
.cards{display:flex;justify-content:center;gap:60px;margin-top:60px}
.card{width:310px;height:330px;background:#fff;box-shadow:0 4px 18px rgba(0,0,0,.18);padding:14px;display:flex;flex-direction:column;align-items:center}
.card-photo{width:100%;height:250px}
.card .btn{margin-top:20px}
.blog-area{position:absolute;top:1260px;left:0;width:1200px;height:980px;background:linear-gradient(180deg,#ffffff 0%,#eef1f5 30%,#e4e8ee 70%,#ffffff 100%)}
.blog-title{position:absolute;top:265px;width:100%;text-align:center}
.posts{position:absolute;top:360px;left:0;width:100%;display:flex;justify-content:center;gap:80px}
.post{width:290px;height:380px;background:#fff;box-shadow:0 4px 16px rgba(0,0,0,.15);padding:14px;font-size:12px;line-height:1.5}
.post-photo{height:200px;margin-bottom:14px}
.post h3{font-size:14px;font-weight:600;color:var(--navy);margin-bottom:6px}
.post .btn{margin-top:10px;padding:7px 16px;font-size:10px}
.all-posts{position:absolute;top:870px;width:100%;text-align:center}
.footer{position:absolute;top:2240px;left:0;width:1200px;height:400px;background:var(--footer);color:#fff;padding:60px 60px}
.footer h4{font-size:20px;font-weight:600;margin-bottom:28px}
.contact li{list-style:none;display:flex;align-items:center;gap:12px;font-size:13px;margin-bottom:18px}
.contact svg{width:16px;height:16px;fill:#fff}
.newsletter{position:absolute;left:800px;top:60px;width:340px;font-size:13px}
.newsletter p{margin-bottom:26px;line-height:1.5}
.newsletter label{display:block;font-size:12px;margin-bottom:6px}
.newsletter .field{height:34px;background:#fff;border-radius:3px}
.newsletter .btn{margin-top:14px;padding:9px 20px}
.legal{position:absolute;top:2640px;left:0;width:1200px;height:36px;background:var(--footer-bottom);color:#c9cde6;font-size:11px;display:flex;align-items:center;padding:0 60px}
</style>
</head>
<body>
<div class="topbar">NEED HELP? TALK TO AN EXPERT: 888-555-0142</div>
<header class="header">
  <div class="brand"><span class="brand-mark"></span><span class="brand-name">TARNWICK</span></div>
  <nav class="nav"><span class="active">HOME</span><span>ABOUT US ▾</span><span>SERVICES ▾</span><span>BLOG</span></nav>
</header>

<section class="hero" role="img" aria-label="Floating white cubes over a soft blue network backdrop">
  <div class="hero-copy">
    <h1>Innovative EPM Solutions for Finance and Beyond</h1>
    <p>Tarnwick Consulting provides decades of experience implementing Veritan EPM products with unique and innovative solutions to challenging business process not only in Finance and Accounting, but across organizations.</p>
    <span class="btn">CONSULTATION</span>
  </div>
</section>

<section class="services">
  <h2 class="section-title">Services</h2>
  <p class="section-sub">Tarnwick Consulting offers services across the entire stack of on-premises and cloud products from Veritan.</p>
  <div class="cards">
    <div class="card"><div class="card-photo" role="img" aria-label="Darts striking a target board" style="background:linear-gradient(135deg,#e9e4d8,#7a6d5a)"></div><span class="btn">BUDGETING AND FORECASTING</span></div>
    <div class="card"><div class="card-photo" role="img" aria-label="Calculator and financial documents" style="background:linear-gradient(135deg,#d9dde2,#8c939c)"></div><span class="btn">CLOSE AND CONSOLIDATION</span></div>
    <div class="card"><div class="card-photo" role="img" aria-label="Magnifying glass over a financial chart" style="background:linear-gradient(135deg,#e3ecf1,#7ea1b8)"></div><span class="btn">REPORTING AND ANALYSIS</span></div>
  </div>
</section>

<section class="blog-area" role="img" aria-label="Faded office towers backdrop">
  <h2 class="section-title blog-title">Recent Blog Posts</h2>
  <div class="posts">
    <article class="post"><div class="post-photo" role="img" aria-label="Laptop on a desk" style="background:linear-gradient(135deg,#5c6470,#c6ccd4)"></div><h3>Veritan Cloud EPM Update — October</h3><p>This month's Cloud EPM highlights series. This month, there are a</p><span class="btn">Read More</span></article>
    <article class="post"><div class="post-photo" role="img" aria-label="Award winners announcement graphic" style="background:linear-gradient(135deg,#1b2a6b,#3b4fa0)"></div><h3>Award Winners</h3><p>We are pleased to announce that our team received the award for his presentation.</p><span class="btn">Read More</span></article>
    <article class="post"><div class="post-photo" role="img" aria-label="Laptop on a desk" style="background:linear-gradient(135deg,#5c6470,#c6ccd4)"></div><h3>Veritan Cloud EPM Update — September</h3><p>Veritan Cloud EPM update highlights series. This month, there are a</p><span class="btn">Read More</span></article>
  </div>
  <div class="all-posts"><span class="btn">SEE ALL BLOG POSTS</span></div>
</section>

<footer class="footer">
  <h4>Company Address</h4>
  <ul class="contact">
    <li><svg viewBox="0 0 24 24"><path d="M12 2a7 7 0 0 0-7 7c0 5 7 13 7 13s7-8 7-13a7 7 0 0 0-7-7zm0 9.5A2.5 2.5 0 1 1 12 6.5a2.5 2.5 0 0 1 0 5z"/></svg>2210 Meridian Parkway, Suite 300, Halden, Texas 75099</li>
    <li><svg viewBox="0 0 24 24"><path d="M6.6 10.8a15 15 0 0 0 6.6 6.6l2.2-2.2a1 1 0 0 1 1-.25 11 11 0 0 0 3.6.6 1 1 0 0 1 1 1V20a1 1 0 0 1-1 1A17 17 0 0 1 3 4a1 1 0 0 1 1-1h3.5a1 1 0 0 1 1 1 11 11 0 0 0 .6 3.6 1 1 0 0 1-.25 1z"/></svg>Phone: (888) 555-0142</li>
    <li><svg viewBox="0 0 24 24"><path d="M3 5h18v14H3zm2 2v.5l7 4.5 7-4.5V7z"/></svg>Email: info@tarnwickconsulting.com</li>
  </ul>
  <div class="newsletter">
    <h4>Newsletter</h4>
    <p>Subscribe to our newsletter to see the latest content we have to offer!</p>
    <label>Email</label>
    <div class="field"></div>
    <span class="btn">Submit</span>
  </div>
</footer>
<div class="legal">© Tarnwick Consulting, LLC All Rights Reserved</div>
</body>
</html>
```